WALKING FOOD TOURISM BUSINESS. REQUEST FOR DIGITAL BROCHURE

Our business is a walking food tourism business in and around Melbourne's central city. We are needing a e-digital brochure - to be solely used as email' marketing content, not print. Therefore PDF size needs to be appropriate/suitable. Please see attached written content required for the brochure - together with our logo. For images, I am happy for designer to use our website content (www.wanderplatekitchen.com). OR any other appropriate and creative 'foodie' or Melbourne image suitable. Many thanks:)

Target Market(s)

Premium brand travellers or local adventurous Australians.

Requirements
Must have
• Quality font and images
Nice to have
• Quality Melbourne and food images. See website - wanderplatekitchen.com
Should not have
• Too much colour. Brand is black and white, sophisticated, premium product.

```html
<!DOCTYPE html>
<html lang="en">
<head>
<meta charset="utf-8">
<title>Wanderplate Kitchen – Brochure Spread</title>
<link href="https://fonts.googleapis.com/css2?family=Montserrat:wght@600;700&family=Work+Sans:wght@400;500;600&display=swap" rel="stylesheet">
<style>
:root{
  --board:#6b6c70;
  --paper:#ffffff;
  --ink:#1a1a1a;
  --body:#555555;
  --rule:#222222;
  --night:#000000;
  --night-box:#111111;
}
*{margin:0;padding:0;box-sizing:border-box}
html,body{width:1200px;height:1200px;overflow:hidden}
body{background:var(--board);position:relative;font-family:"Work Sans",sans-serif;color:var(--ink)}
.page{position:absolute;width:247px;height:350px;background:var(--paper);box-shadow:3px 4px 8px rgba(0,0,0,.35);overflow:hidden}
.photo{position:absolute}
.heading{position:absolute;left:14px;top:14px;font-family:"Montserrat",sans-serif;font-weight:700;font-size:10.5px;letter-spacing:.1px;white-space:nowrap}
.heading::after{content:"";position:absolute;left:0;top:17px;width:25px;height:2px;background:var(--ink)}
.tour-name{position:absolute;left:14px;top:42px;font-weight:600;font-size:7px;padding-bottom:2px;border-bottom:.7px solid var(--ink);white-space:nowrap}
.facts{position:absolute;left:14px;top:64px;font-size:4.3px;line-height:9px;display:grid;grid-template-columns:30px 30px 30px 30px;white-space:nowrap}
.facts b{font-weight:600}
.copy{position:absolute;left:14px;width:194px;font-size:4.5px;line-height:6.6px;color:var(--body)}
.copy p{margin-bottom:3.5px}
.copy em{font-style:italic}
.thumbs{position:absolute;left:14px;top:88px;display:flex;gap:3px}
.thumbs span{width:62px;height:62px;display:block}
.footer-name{position:absolute;left:14px;top:324px;font-size:5.5px;font-weight:600;color:var(--ink);white-space:nowrap}
.footer-rule{position:absolute;left:65px;right:14px;top:333px;height:.6px;background:var(--rule)}
.folio{position:absolute;right:14px;top:336px;font-size:3.6px;font-weight:500}
.cover-name{position:absolute;left:0;right:0;top:283px;text-align:center;font-size:10px;font-weight:600}
.back{background:var(--night);color:#fff}
.back-mark{position:absolute;left:68px;top:210px;width:111px;height:65px;background:var(--night-box);display:flex;align-items:center;justify-content:center;font-size:8.5px;font-weight:600}
.back-info{position:absolute;left:0;right:0;top:283px;text-align:center;font-size:4.3px;line-height:5.6px}
.back-info .label{font-weight:600}
.phone{display:inline-block;background:#fff;color:#000;padding:0 5px;margin:2px 0 1px;font-weight:500}
.social{display:flex;justify-content:center;align-items:center;gap:2px}
.social i{width:3px;height:3px;border-radius:50%;background:#fff;display:inline-block}
.terms{margin-top:7px;font-size:3px;line-height:3.8px}
.terms .label{font-size:3.3px}
</style>
</head>
<body>

<section class="page" style="left:71px;top:235px">
  <div class="photo" role="img" aria-label="Plated restaurant dish with greens on a white plate in a warm dining room" style="left:0;top:51px;width:247px;height:162px;background:linear-gradient(135deg,#5c4a3a,#a58a6e 45%,#e4e0da 60%,#6e5846)"></div>
  <div class="cover-name">Wanderplate Kitchen</div>
</section>

<section class="page" style="left:342px;top:235px">
  <h2 class="heading">ABOUT US</h2>
  <div class="copy" style="top:40px;width:101px;text-align:justify">
    <p>We craft walking adventures for travellers and locals alike - all seen through the lens of remarkable food. Each of our tours shares the spirit of the city, its people and layered past - pausing to sip, taste and linger at favourite local kitchens &amp; enjoying the dishes they do best.</p>
  </div>
  <div class="photo" role="img" aria-label="Historic brick tower rising beneath a glass cone roof" style="left:130px;top:0;width:117px;height:350px;background:linear-gradient(180deg,#6f7f92,#9c8a72 30%,#c08a5a 60%,#9b6c45)"></div>
  <div class="footer-name">Wanderplate Kitchen</div>
</section>

<section class="page" style="left:612px;top:235px">
  <h2 class="heading">OUR EXPERIENCES</h2>
  <h3 class="tour-name">Laneway Tasting Trail</h3>
  <div class="facts"><b>TIME</b><span>: 3.5 Hrs</span><b>GUESTS</b><span>: Up to 8</span><b>FOR ADULT</b><span>: A$165</span><b>FOR CHILD</b><span>: A$115</span></div>
  <div class="thumbs">
    <span role="img" aria-label="Colourful salad in a ceramic bowl" style="background:linear-gradient(135deg,#5a3a22,#b5542e)"></span>
    <span role="img" aria-label="Light seafood dish in a white bowl" style="background:linear-gradient(135deg,#cfc8bb,#d8a94a)"></span>
    <span role="img" aria-label="Glazed chicken wings on a blue plate" style="background:linear-gradient(135deg,#3f4a5a,#8a4a22)"></span>
  </div>
  <div class="copy" style="top:163px">
    <p>Love good food? Can never decide where to eat next and worry you are missing the places locals really rate? If that sounds like you, then our Laneway Tasting Trail is the tour made for you.</p>
    <p>Short on time, our Tasting Trail packs the best into one afternoon - sampling signature plates as you wander the hidden lanes of the city’s lively dining heart.</p>
  </div>
  <div class="footer-name">Wanderplate Kitchen</div><div class="footer-rule"></div><div class="folio">03</div>
</section>

<section class="page" style="left:881px;top:235px">
  <h2 class="heading">OUR EXPERIENCES</h2>
  <h3 class="tour-name">Night Market Bites Walk</h3>
  <div class="facts"><b>TIME</b><span>: 3 Hrs</span><b>GUESTS</b><span>: Up to 10</span><b>FOR ADULT</b><span>: A$105</span><b>FOR CHILD</b><span>: A$65</span></div>
  <div class="thumbs">
    <span role="img" aria-label="Filled steamed buns" style="background:linear-gradient(135deg,#d9d2c6,#8a5a4a)"></span>
    <span role="img" aria-label="Tray of golden egg tarts" style="background:linear-gradient(135deg,#c98a3a,#e6b24a)"></span>
    <span role="img" aria-label="Dessert on a dark plate" style="background:linear-gradient(135deg,#151515,#6a1a22)"></span>
  </div>
  <div class="copy" style="top:163px">
    <p>Peckish? Then grab your appetite and HEAD OUT AFTER DARK - the way the city does it. Our Night Market Bites Walk suits visitors and locals who love to roam, discover &amp; try the best of the Asian street food scene.</p>
    <p>Eat your way through busy stalls and tiny kitchens – trying fragrant noodles, handmade dumplings, sizzling skewers, sweet buns and more – while hearing the stories of the many families who brought these flavours here over the generations.</p>
    <p><em>A great way to find a few of the city’s best kept food secrets.</em></p>
  </div>
  <div class="footer-name">Wanderplate Kitchen</div><div class="footer-rule"></div><div class="folio">04</div>
</section>

<section class="page" style="left:71px;top:615px">
  <h2 class="heading">OUR EXPERIENCES</h2>
  <h3 class="tour-name">City Stories Stroll</h3>
  <div class="facts"><b>TIME</b><span>: 2.5 Hrs</span><b>GUESTS</b><span>: Up to 12</span><b>FOR ADULT</b><span>: A$85</span><b>FOR CHILD</b><span>: A$45</span></div>
  <div class="copy" style="top:88px">
    <p>From the riverbank to famous laneways, heritage streets, grand theatres &amp; churches - uncover the spirit, culture &amp; people of our wonderful, ever-changing city.</p>
    <p>Join us on foot as we share tales of the city’s past and present. Along the way you’ll see the places that shaped it, from its earliest days – right up to now, and learn why it remains one of the most diverse and welcoming cities on earth.</p>
  </div>
  <div class="photo" role="img" aria-label="Riverside waterfront with city towers and boats" style="left:14px;top:147px;width:130px;height:93px;background:linear-gradient(180deg,#7f9cc4,#9aa3a8 55%,#4a5a66)"></div>
  <div class="photo" role="img" aria-label="City tram passing a historic building" style="left:147px;top:176px;width:63px;height:64px;background:linear-gradient(180deg,#d6d8dc,#8a7a6a 60%,#4a7a4a)"></div>
  <div class="photo" role="img" aria-label="Ornate heritage shopping arcade" style="left:81px;top:243px;width:63px;height:63px;background:linear-gradient(180deg,#6a4a32,#b58a5a,#5a3a28)"></div>
  <div class="footer-name">Wanderplate Kitchen</div><div class="footer-rule"></div><div class="folio">05</div>
</section>

<section class="page" style="left:342px;top:615px">
  <h2 class="heading">OUR EXPERIENCES</h2>
  <h3 class="tour-name">Twilight Table &amp; Wine</h3>
  <div class="facts"><b>TIME</b><span>: 3 Hrs</span><b>GUESTS</b><span>: Up to 8</span><b>FOR ADULT</b><span>: A$210</span><b>FOR CHILD</b><span>: A$150</span></div>
  <div class="thumbs">
    <span role="img" aria-label="Cheese and charcuterie platter with wine" style="background:linear-gradient(135deg,#e6dccb,#8a3a2a)"></span>
    <span role="img" aria-label="Guests seated at a restaurant table" style="background:linear-gradient(135deg,#c9c2b6,#5a4a3a)"></span>
    <span role="img" aria-label="Dessert on a dark plate" style="background:linear-gradient(135deg,#151515,#6a1a22)"></span>
  </div>
  <div class="copy" style="top:160px">
    <p>Spend your evening in one of the city’s liveliest, most delicious and tempting dining quarters.</p>
    <p>You’ll be charmed by warm hospitality as you taste standout dishes from some of our favourite kitchens - matching each course with a well chosen glass – and hearing how this quarter grew into the much loved food destination it is now.</p>
  </div>
  <div class="footer-name">Wanderplate Kitchen</div><div class="footer-rule"></div><div class="folio">06</div>
</section>

<section class="page" style="left:612px;top:615px">
  <h2 class="heading">PRIVATE EXPERIENCES</h2>
  <div style="position:absolute;left:14px;top:42px;font-size:4.3px;font-weight:600">UP TO 8 HOURS / TAILORED ITINERARIES</div>
  <div class="copy" style="top:55px">
    <p>Our private tours are perfect for a relaxed and fun group day out. Share and enjoy the flavours of the city with friends – perhaps a team outing, a family get-together, a milestone birthday or a wedding party. All with your own dedicated tour host.</p>
    <p>Choose from one of our <b style="color:var(--ink);font-weight:600">Wanderplate Kitchen Experiences</b> – with the option to adjust the tour length, start time and distance walked. OR design your own day around your interests, theme, community or corporate group. Either way, your PRIVATE EXPERIENCE will be shaped around you.</p>
    <p style="color:var(--ink)">Enquiries: info@wanderplatekitchen.com</p>
  </div>
  <div class="photo" role="img" aria-label="Glass of white wine in front of a vineyard at dusk" style="left:14px;top:137px;width:143px;height:91px;background:linear-gradient(180deg,#a89a74,#5a5a2a 50%,#2a3218)"></div>
  <div class="footer-name">Wanderplate Kitchen</div><div class="footer-rule"></div><div class="folio">07</div>
</section>

<section class="page back" style="left:881px;top:615px">
  <div class="back-mark">Wanderplate Kitchen</div>
  <div class="back-info">
    <div class="label">FOR BOOKING SCHEDULE &amp; ENQUIRY</div>
    <div class="phone">+61 400 555 019</div>
    <div class="social"><i></i>wanderplate.kitchen</div>
    <div class="social"><i></i>Wanderplate.Kitchen</div>
    <div class="terms">
      <div class="label">CANCELLATION &amp; AMENDMENTS</div>
      <div>100% REFUND for cancellations outside 24 hours of the tour departure time</div>
      <div>NO REFUND for cancellations made within 24 hours of the tour departure time</div>
    </div>
  </div>
</section>

</body>
</html>
```